Flyer design for retail store owners

i would need to have a flyer design for my retail shop customers to show that I am a mailbox store that has all major shipping vendors to for their shipping needs. Ensuring that they can take advantage of opening a house account at the store and billed monthly, word document has all the details. Please use stock images for the notary public, passport photos, mailbox brass pictures of my actual mailboxes are listed in the pictures. I need to make it POP and WOW these retail store owners as I am using it to advertise the business

```html
<!DOCTYPE html>
<html lang="en">
<head>
<meta charset="utf-8">
<title>Now Renting Mailboxes – Swift Parcel Hub</title>
<link rel="stylesheet" href="https://fonts.googleapis.com/css2?family=Montserrat:wght@500;800&family=Poppins:wght@400;600;700&family=Oswald:wght@500;600&family=Roboto+Condensed:wght@300&display=swap">
<style>
  :root {
    --teal: #0a91a2;
    --teal-deep: #0b6f8a;
    --teal-light: #6fc4cd;
    --teal-pale: #bdeef3;
    --navy: #063d60;
    --ink: #1f1f1f;
    --accent: #3b2008;
    --white: #ffffff;
  }
  * { margin: 0; padding: 0; box-sizing: border-box; }
  html, body { width: 927px; height: 1200px; overflow: hidden; background: var(--white); }
  .flyer { position: relative; width: 927px; height: 1200px; overflow: hidden; background: var(--white); font-family: "Poppins", sans-serif; color: var(--ink); }

  .header-band {
    position: absolute; left: 0; top: 0; width: 927px; height: 233px;
    background: linear-gradient(135deg, #0b7f95 0%, var(--teal) 45%, #0b8ea0 100%);
  }
  .header-shadow {
    position: absolute; left: 60px; top: 232px; width: 480px; height: 14px;
    background: radial-gradient(ellipse at top, rgba(0,0,0,.35), rgba(0,0,0,0) 70%);
  }
  .title-plate {
    position: absolute; left: 33px; top: 27px; width: 527px; height: 78px;
    background: var(--navy); border-radius: 38px 38px 0 38px;
  }
  .title-main {
    position: absolute; left: 52px; top: 28px;
    font-family: "Montserrat", sans-serif; font-weight: 800; font-size: 64px; line-height: 78px;
    color: #f2f2f2; letter-spacing: -0.5px; white-space: nowrap;
  }
  .title-sub {
    position: absolute; left: 50px; top: 112px;
    font-family: "Montserrat", sans-serif; font-weight: 500; font-size: 63px; line-height: 70px;
    color: var(--white); letter-spacing: 0.5px; white-space: nowrap;
  }
  .title-place {
    position: absolute; left: 90px; top: 183px;
    font-family: "Oswald", sans-serif; font-weight: 600; font-size: 31px; line-height: 40px;
    color: var(--white); transform: scaleX(0.82); transform-origin: left; white-space: nowrap;
  }

  .photo-main {
    position: absolute; left: 538px; top: 42px; width: 520px; height: 520px; border-radius: 50%;
    border: 14px solid var(--teal-light);
    background: radial-gradient(circle at 40% 45%, #e8b86a 0%, #c98f3c 40%, #6b4218 85%);
  }
  .photo-detail {
    position: absolute; left: 664px; top: 426px; width: 300px; height: 326px; border-radius: 50%;
    border: 16px solid var(--teal-light);
    background: radial-gradient(circle at 55% 50%, #e4b765 0%, #b47d30 55%, #5e3a14 100%);
  }
  .open-view { position: absolute; left: 700px; top: 730px; width: 220px; height: 90px; }

  .dot { position: absolute; border-radius: 50%; background: var(--teal-pale); }

  .intro {
    position: absolute; left: 22px; top: 254px; width: 484px;
    font-size: 16.1px; line-height: 24.3px; text-align: justify; color: var(--ink);
  }
  .intro strong { font-weight: 700; }

  .band-offering {
    position: absolute; left: 0; top: 520px; width: 670px; height: 48px; line-height: 48px; padding-left: 78px;
    background: var(--teal); font-family: "Oswald", sans-serif; font-weight: 500; color: var(--white);
    letter-spacing: 2.5px; font-size: 28px; white-space: nowrap;
  }
  .deals-arrow { position: absolute; left: 0; top: 767px; width: 540px; height: 55px; }
  .deals-title {
    position: absolute; left: 78px; top: 767px; line-height: 55px; white-space: nowrap;
    font-family: "Oswald", sans-serif; font-weight: 500; font-size: 26px; letter-spacing: 2px; color: var(--white);
  }

  .offer-list { position: absolute; left: 0; top: 576px; width: 660px; list-style: none; }
  .offer-list li { position: relative; padding-left: 78px; font-size: 17.6px; line-height: 19px; margin-bottom: 18px; }
  .offer-list li::before {
    content: ""; position: absolute; left: 48px; top: 7px;
    border-left: 12px solid #2b1608; border-top: 6.5px solid transparent; border-bottom: 6.5px solid transparent;
  }
  .offer-list strong { font-weight: 700; }
  .promo-price { display: inline-block; border: 1.5px dashed #222; border-radius: 10px; padding: 0 6px; font-weight: 700; }

  .deals-bracket {
    position: absolute; left: 48px; top: 832px; width: 52px; height: 243px;
    border-left: 1.5px solid var(--teal-deep); border-top: 1.5px solid var(--teal-deep); border-bottom: 1.5px solid var(--teal-deep);
  }
  .deal-list { position: absolute; left: 0; top: 840px; width: 892px; list-style: none; }
  .deal-list li { position: relative; padding-left: 78px; font-size: 17.6px; line-height: 22px; }
  .deal-list strong { color: var(--accent); font-weight: 700; }
  .deal-icon { position: absolute; left: 30px; top: 3px; width: 16px; height: 11px; }
  .deal-tick { position: absolute; left: 48px; top: 8px; width: 12px; border-top: 1.5px solid var(--teal-deep); }

  .footer { position: absolute; left: 0; top: 1095px; width: 927px; height: 105px; background: var(--teal-deep); }
  .footer-left {
    position: absolute; left: 0; top: 1095px; width: 360px; height: 105px;
    background: linear-gradient(90deg, #2ea6a6 0%, #3aaea8 100%);
  }
  .footer-curl { position: absolute; left: 300px; top: 1068px; width: 80px; height: 132px; }
  .brand { position: absolute; left: 26px; top: 1115px; display: flex; align-items: center; gap: 14px; }
  .brand-mark { width: 62px; height: 62px; border-radius: 50%; background: rgba(255,255,255,.22); }
  .brand-name { font-family: "Poppins", sans-serif; font-weight: 600; font-size: 25px; line-height: 25px; color: var(--white); white-space: nowrap; }

  .offer-clock { position: absolute; left: 372px; top: 1120px; width: 62px; height: 62px; }
  .offer-text {
    position: absolute; left: 444px; top: 1124px; white-space: nowrap;
    font-family: "Roboto Condensed", sans-serif; font-weight: 300; font-size: 40px; line-height: 56px; color: var(--white);
  }
</style>
</head>
<body>
<div class="flyer">

  <div class="header-band"></div>
  <div class="header-shadow"></div>
  <div class="title-plate"></div>
  <h1 class="title-main">NOW RENTING</h1>
  <div class="title-sub">MAILBOXES ON</div>
  <div class="title-place">MAPLEWOOD COMMONS SHOPPING CENTER.</div>

  <div class="photo-main" role="img" aria-label="Brass mailbox bank with rows of small locking doors"></div>
  <div class="photo-detail" role="img" aria-label="Close-up of an open brass mailbox door"></div>
  <svg class="open-view" viewBox="0 0 220 90">
    <path id="openViewArc" d="M12 20 Q110 58 205 22" fill="none"/>
    <text font-family="Montserrat, sans-serif" font-weight="800" font-size="30" fill="#6fc4cd" letter-spacing="1">
      <textPath href="#openViewArc">OPEN VIEW</textPath>
    </text>
  </svg>

  <div class="dot" style="left:656px;top:774px;width:30px;height:30px;"></div>
  <div class="dot" style="left:730px;top:794px;width:48px;height:48px;"></div>
  <div class="dot" style="left:711px;top:872px;width:20px;height:20px;"></div>

  <p class="intro"><strong>Renting a mail box</strong> is one of the most efficient and cost saving methods for receiving your mail and packages. Instead of having to worry about private security, weather conditions, sorting, and deliveries; all you have to do is pick-up your mail from our secured facility each day except Sundays. You will get a notification when mail arrives whether envelope or package, it will be scanned in daily which other mailbox stores do not offer! We offer onsite Notary Public with no appointments and onsite Passport Photos and can ship out same day.</p>

  <h2 class="band-offering">WE ARE OFFERING-</h2>

  <ul class="offer-list">
    <li>All Maplewood Commons shopping center owners/employees an exclusive promo deal! <span class="promo-price">$12 a month for 6-12 months leases!</span></li>
    <li>You get a mailbox in the shop,</li>
    <li>A book of <strong>stamps(20 count)</strong>, &nbsp;3 notarizations by appointment, <strong>100 copies</strong> of black and white, and <strong>100 copies</strong> of color.<br>Please see associate for sign up!</li>
  </ul>

  <svg class="deals-arrow" viewBox="0 0 540 55" aria-hidden="true">
    <polygon points="0,0 470,0 495,27.5 470,55 0,55" fill="#0a91a2"/>
    <polyline points="484,3 530,27.5 484,52" fill="none" stroke="#0a91a2" stroke-width="6"/>
  </svg>
  <h2 class="deals-title">CHECK OUT THESE OTHER DEALS!</h2>

  <div class="deals-bracket"></div>
  <ul class="deal-list">
    <li><svg class="deal-icon" viewBox="0 0 16 11"><rect width="16" height="11" rx="1" fill="#0a91a2"/><polyline points="1,1 8,6 15,1" fill="none" stroke="#fff" stroke-width="1.3"/></svg><span class="deal-tick"></span>As a retail owner, you know how important it is to keep your customers coming back - you will get <strong>20% discount</strong> for printing services.</li>
    <li style="margin-top:16px;"><svg class="deal-icon" viewBox="0 0 16 11"><rect width="16" height="11" rx="1" fill="#0a91a2"/><polyline points="1,1 8,6 15,1" fill="none" stroke="#fff" stroke-width="1.3"/></svg><span class="deal-tick"></span>We duplicate keys for <strong>$2/each,</strong> our regular price charge is <strong>$4/each</strong>. Save up to <strong>50%!</strong></li>
    <li style="margin-top:12px;"><svg class="deal-icon" viewBox="0 0 16 11"><rect width="16" height="11" rx="1" fill="#0a91a2"/><polyline points="1,1 8,6 15,1" fill="none" stroke="#fff" stroke-width="1.3"/></svg><span class="deal-tick"></span>Lamination is also <strong>discounted at 10%</strong> off.</li>
    <li style="margin-top:12px;"><svg class="deal-icon" viewBox="0 0 16 11"><rect width="16" height="11" rx="1" fill="#0a91a2"/><polyline points="1,1 8,6 15,1" fill="none" stroke="#fff" stroke-width="1.3"/></svg><span class="deal-tick"></span><strong>10%</strong> off retail supplies … must be minimum of 10$</li>
    <li style="margin-top:12px;"><svg class="deal-icon" viewBox="0 0 16 11"><rect width="16" height="11" rx="1" fill="#0a91a2"/><polyline points="1,1 8,6 15,1" fill="none" stroke="#fff" stroke-width="1.3"/></svg><span class="deal-tick"></span>For house accounts -a <strong>5%</strong> discount will be deducted monthly of billing change to invoicing PLUS we're giving another <strong>5%</strong> of the discount if you upgrade and sign up for mailbox. Great right?</li>
  </ul>

  <footer>
    <div class="footer"></div>
    <div class="footer-left"></div>
    <svg class="footer-curl" viewBox="0 0 80 132" aria-hidden="true">
      <path d="M0 27 L50 27 Q70 10 68 0 Q60 70 30 132 L0 132 Z" fill="#2a9e9c"/>
      <path d="M68 0 Q60 70 30 132 L60 132 Q75 60 68 0 Z" fill="#0b6f8a"/>
    </svg>
    <div class="brand">
      <div class="brand-mark"></div>
      <div class="brand-name">SWIFT<br>PARCEL HUB</div>
    </div>
    <svg class="offer-clock" viewBox="0 0 62 62" aria-hidden="true">
      <circle cx="31" cy="34" r="23" fill="none" stroke="#fff" stroke-width="5"/>
      <path d="M6 16 A12 12 0 0 1 20 5" fill="none" stroke="#fff" stroke-width="5" stroke-linecap="round"/>
      <path d="M56 16 A12 12 0 0 0 42 5" fill="none" stroke="#fff" stroke-width="5" stroke-linecap="round"/>
      <polyline points="31,22 31,35 40,35" fill="none" stroke="#fff" stroke-width="5" stroke-linecap="round"/>
      <line x1="14" y1="54" x2="10" y2="59" stroke="#fff" stroke-width="4" stroke-linecap="round"/>
      <line x1="48" y1="54" x2="52" y2="59" stroke="#fff" stroke-width="4" stroke-linecap="round"/>
    </svg>
    <div class="offer-text">LIMITED TIME OFFER NOW!</div>
  </footer>

</div>
</body>
</html>
```